create a webpage for optometry practice

I'm looking to create a professional and elegant webpage for my practice. I prefer neutral earthy colors, but I am open to other ideas. I have included an image of my logo to be used in the process. This will be a page that will illustrate information about my practice and the kind of services we offer. I am in process of having the practice remodeled. So I don't have any photos of my practice to include yet.

Target Market(s)

My practice serves young and mature families.

Industry/Entity Type

It Professional

Number of Pages Required

5+ page

Font styles to use
Sans Serif

Colors
33a6d7
86cfc6
85cae6
cadf82
3276b5
faa54b
abd036
f78c1e

Requirements
Must have
• I would need to incorporate information about my practice, services, insurance accepted, make appointment, contact us, and about our family.
Nice to have
• I would like to see something fresh, modern, and unique

```html
<!DOCTYPE html>
<html lang="en">
<head>
<meta charset="utf-8">
<title>Lumora Eye Care</title>
<link href="https://fonts.googleapis.com/css2?family=Roboto:wght@300;400;500;700&family=Great+Vibes&display=swap" rel="stylesheet">
<style>
:root{
  --teal:#86cfc6;
  --teal-dark:#6fc0b6;
  --sky:#85cae6;
  --blue:#33a6d7;
  --orange:#f78c1e;
  --orange-soft:#faa54b;
  --green:#b5d66a;
  --ink:#222;
  --text:#666;
  --muted:#999;
  --footer:#ececec;
  --panel:#e8e8e8;
  --hero-bg:#f6e6df;
  --hero-mid:#e8d2c6;
  --hero-warm:#b89a80;
  --room-light:#f4f6f7;
  --room-mid:#dde3e7;
}
*{box-sizing:border-box;margin:0;padding:0}
html,body{width:1200px;height:2286px;overflow:hidden;background:#fff}
body{position:relative;font-family:"Roboto",Arial,sans-serif;color:var(--text)}
.abs{position:absolute}

/* header */
.brand{left:74px;top:48px;display:flex;align-items:center;gap:10px;white-space:nowrap}
.brand-dot{width:26px;height:26px;border-radius:50%;background:var(--orange);flex:none}
.brand-name{font-size:28px;font-weight:400;color:#4a4a4a;letter-spacing:1px;line-height:1;white-space:nowrap}
.contact-top{right:74px;top:26px;text-align:right;font-size:13px;color:#555;line-height:30px}
.contact-top b{color:var(--orange);font-weight:700}
.socials{display:flex;gap:6px;justify-content:flex-end;margin-top:4px}
.socials span{width:26px;height:26px;border:1.5px solid #aaa;border-radius:50%;display:block}

/* nav */
.nav{left:74px;top:143px;width:1052px;height:38px;background:var(--teal);display:flex;align-items:center;padding-left:16px}
.nav a{color:#fff;text-decoration:none;font-size:13px;font-weight:500;margin-right:50px;text-transform:uppercase}
.search{position:absolute;right:6px;top:6px;width:212px;height:26px;background:#fff;font-size:11px;color:var(--muted);padding:6px 8px}
.search svg{position:absolute;right:6px;top:6px}

/* hero */
.hero{left:74px;top:194px;width:1052px;height:459px;
  background:
    radial-gradient(ellipse 22% 30% at 49% 50%, rgba(150,120,90,.75) 0%, rgba(184,154,128,.45) 45%, rgba(184,154,128,0) 100%),
    radial-gradient(ellipse 40% 50% at 52% 48%, var(--hero-mid) 0%, rgba(232,210,198,0) 100%),
    linear-gradient(90deg,#fbf8f6 0%,var(--hero-bg) 30%,var(--hero-bg) 100%)}
.hero-tag{left:920px;top:231px;background:var(--orange-soft);color:#fff;font-size:15px;padding:4px 10px}
.hero-title{left:850px;top:262px;width:250px;text-align:right;font-size:22px;font-weight:500;color:#111}
.hero-script{left:820px;top:552px;font-family:"Great Vibes",cursive;font-size:30px;color:#8a7d78}
.hero-dots{left:1034px;top:614px;display:flex;gap:3px}
.hero-dots i{width:10px;height:10px;background:#fff;opacity:.7;display:block}

/* welcome */
.welcome{left:74px;top:691px;width:370px}
h2{font-size:24px;font-weight:500;color:var(--ink)}
.welcome p{margin-top:20px;font-size:13px;line-height:24px}
.btn-outline{display:inline-block;margin-top:16px;border:1.5px solid var(--teal);color:var(--teal-dark);font-size:12px;padding:8px 14px;text-transform:uppercase}
.service{top:691px;width:212px;height:252px;color:#fff;text-align:center;padding:20px 20px 0}
.service .icon{width:90px;height:78px;margin:0 auto;border-radius:50%;background:rgba(255,255,255,.35)}
.service h3{margin-top:42px;font-size:15px;font-weight:500;text-transform:uppercase}
.service p{margin-top:12px;font-size:12.5px;line-height:21px}
.s-exam{left:470px;background:var(--sky)}
.s-lens{left:691px;background:var(--orange-soft)}
.s-lasik{left:912px;background:var(--green)}

/* appointment */
.appt{left:74px;top:1006px;width:332px;height:567px;background:var(--panel)}
.appt-head{height:105px;background:var(--sky);color:#fff;text-align:center;padding-top:16px}
.appt-head h3{font-size:24px;font-weight:400}
.appt-phone{margin-top:4px;font-size:23px;font-weight:300;display:flex;justify-content:center;align-items:center;gap:8px}
.appt-phone span{width:30px;height:30px;border-radius:50%;background:var(--blue);display:flex;align-items:center;justify-content:center}
.or{position:absolute;left:151px;top:90px;width:30px;height:30px;border-radius:50%;background:var(--orange);color:#fff;font-size:11px;line-height:30px;text-align:center}
.field{position:absolute;left:27px;width:276px;height:32px;background:#fff;border:1px solid #ddd;font-size:12px;color:var(--muted);padding:8px 10px}
.captcha{position:absolute;left:162px;top:459px;width:84px;height:30px;background:#fff;border:1px solid #ddd;color:var(--orange);font-size:16px;text-align:center;line-height:28px;letter-spacing:1px}
.submit{position:absolute;left:27px;top:506px;width:137px;height:29px;background:var(--orange);color:#fff;font-size:12px;font-weight:700;text-align:center;line-height:29px}

/* practice */
.doctor{left:440px;top:1010px;width:686px;height:380px;
  background:linear-gradient(160deg,var(--room-light) 0%,var(--room-mid) 55%,#cfd6db 100%);
  -webkit-mask-image:linear-gradient(90deg,transparent 0%,#000 28%,#000 90%,transparent 100%),linear-gradient(180deg,transparent 0%,#000 12%,#000 75%,transparent 100%);
  -webkit-mask-composite:source-in;
  mask-image:linear-gradient(90deg,transparent 0%,#000 28%,#000 90%,transparent 100%),linear-gradient(180deg,transparent 0%,#000 12%,#000 75%,transparent 100%);
  mask-composite:intersect}
.about{left:434px;top:1410px;width:692px}
.about p{margin-top:16px;font-size:13px;line-height:24px}

/* testimonials */
.say{left:74px;top:1620px}
.avatar{left:88px;top:1676px;width:107px;height:107px;border-radius:50%;background:linear-gradient(#c9d8e4,#9fb2bf)}
.quote-mark{left:226px;top:1664px;font-size:56px;color:#bbb;font-weight:700;line-height:1}
.quote{left:261px;top:1680px;width:864px;font-size:13px;line-height:24px}
.quote-by{left:261px;top:1816px;font-size:12px;color:var(--orange)}
.q-dots{left:130px;top:1818px;display:flex;gap:4px}
.q-dots i{width:9px;height:9px;border-radius:50%;background:#ddd;display:block}
.q-dots i:first-child{background:var(--sky)}

/* newsletter */
.newsletter{left:0;top:1886px;width:1200px;height:95px;background:var(--teal);color:#fff}
.nl-title{position:absolute;left:154px;top:24px;font-size:19px;font-weight:500;line-height:21px;text-transform:uppercase}
.nl-input{position:absolute;left:344px;top:30px;width:298px;height:32px;background:#fff;font-size:12px;color:var(--muted);padding:9px 10px}
.nl-btn{position:absolute;left:651px;top:30px;width:110px;height:32px;background:var(--orange);font-size:13px;font-weight:700;text-align:center;line-height:32px}
.stay{position:absolute;left:882px;top:24px;font-size:19px;font-weight:500;line-height:21px;text-transform:uppercase}
.stay-icons{position:absolute;left:1024px;top:32px;display:flex;gap:6px}
.stay-icons span{width:26px;height:26px;border:1.5px solid #fff;border-radius:50%;display:block}

/* footer */
.footer{left:0;top:1981px;width:1200px;height:305px;background:var(--footer)}
.fcol{position:absolute;top:48px;width:240px;font-size:13px}
.fcol h4{font-size:13px;font-weight:700;color:var(--ink);text-transform:uppercase;margin-bottom:20px}
.post{margin-bottom:26px}
.post small{display:block;font-size:11px;color:var(--muted);margin-bottom:4px}
.post p{line-height:20px;color:#555}
.touch{display:flex;gap:14px;margin-bottom:14px;line-height:20px;color:#555}
.touch span{flex:none;width:30px;height:30px;border-radius:50%;background:#555;display:flex;align-items:center;justify-content:center}
.f-brand{position:absolute;left:912px;top:80px;display:flex;align-items:center;gap:8px}
.f-brand .brand-name{font-size:22px}
.legal{position:absolute;left:884px;top:230px;font-size:12px;line-height:19px;color:#555}
</style>
</head>
<body>

<div class="abs brand"><span class="brand-dot"></span><span class="brand-name">LUMORA EYE</span></div>
<div class="abs contact-top">
  <div><b>CALL US DIRECTLY :</b> 1-800-555-0142</div>
  <div>228, LOREM IPSUM, DOLOR SIT, 898585-LOREM</div>
  <div class="socials"><span></span><span></span><span></span></div>
</div>

<nav class="abs nav">
  <a>Home</a><a>About Us</a><a>Services</a><a>Our Practice</a><a>Appointments</a><a>Blog</a><a>Contact Us</a>
  <div class="search">Enter Your Search
    <svg width="13" height="13" viewBox="0 0 13 13"><circle cx="5.5" cy="5.5" r="4" fill="none" stroke="#86cfc6" stroke-width="1.8"/><line x1="8.5" y1="8.5" x2="12" y2="12" stroke="#86cfc6" stroke-width="1.8"/></svg>
  </div>
</nav>

<div class="abs hero" role="img" aria-label="Close-up of a hazel eye beside an eye test chart"></div>
<div class="abs hero-tag">EXCELLENT EYE CARE</div>
<div class="abs hero-title">FOR THE ENTIRE FAMILY</div>
<div class="abs hero-script">Better Vision for a better life</div>
<div class="abs hero-dots"><i></i><i></i><i></i><i></i><i></i></div>

<section class="abs welcome">
  <h2>Welcome to Lumora Eyecare</h2>
  <p>In publishing and graphic design, lorem ipsum is a filler text commonly used to demonstrate the graphic elements of a document or visual presentation. Replacing meaningful content with placeholder commonly used to demonstrate text allows commonly used to view quickly-generated intoo ic elements of acommonly used to demonstrate document or visual presentation.</p>
  <span class="btn-outline">Read More</span>
</section>

<div class="abs service s-exam"><div class="icon" role="img" aria-label="Eye exam equipment icon"></div><h3>Eye Exams</h3><p>In publishing and graphic design, lorem ipsum is a filler or visual presentation.</p></div>
<div class="abs service s-lens"><div class="icon" role="img" aria-label="Contact lens icon"></div><h3>Contact Lenses</h3><p>In publishing and graphic design, lorem ipsum is a filler or visual presentation.</p></div>
<div class="abs service s-lasik"><div class="icon" role="img" aria-label="Eye icon"></div><h3>Lasik</h3><p>In publishing and graphic design, lorem ipsum is a filler or visual presentation.</p></div>

<section class="abs appt">
  <div class="appt-head">
    <h3>Make an Appointment</h3>
    <div class="appt-phone"><span><svg width="12" height="16" viewBox="0 0 12 16"><rect x="1" y="1" width="10" height="14" rx="2" fill="none" stroke="#fff" stroke-width="1.6"/><circle cx="6" cy="12" r="1" fill="#fff"/></svg></span>1-800-555-0142</div>
  </div>
  <div class="or">OR</div>
  <div class="field" style="top:125px">Full Name</div>
  <div class="field" style="top:172px">Phone Number</div>
  <div class="field" style="top:219px">Email Address</div>
  <div class="field" style="top:266px">Appointment Date</div>
  <div class="field" style="top:327px;height:115px">Message</div>
  <div class="field" style="top:459px;width:120px">Enter Code</div>
  <div class="captcha">mmehx</div>
  <div class="submit">SUBMIT REQUEST</div>
</section>

<div class="abs doctor" role="img" aria-label="Optometrist in a white coat beside exam equipment"></div>
<section class="abs about">
  <h2>About My Practice</h2>
  <p>In publishing and graphic design, lorem ipsum is a filler text commonly used to demonstrate the graphic elements of a document or visual presentation. Replacing meaningful content with placeholder commonly used to demonstrate text allows commonly used to view quickly-generated intoo ic elements of acommonly used to demonstrate document or visual presentation.</p>
</section>

<h2 class="abs say">What Our Patients Say</h2>
<div class="abs avatar" role="img" aria-label="Patient portrait"></div>
<div class="abs quote-mark">&ldquo;</div>
<p class="abs quote">In publishing and graphic design, lorem ipsum is a filler text commonly used to demonstrate the graphic elements of a document or visual presentation. Replacing meaningful content with placeholder commonly used to demonstrate text allows commonly used to view quickly-generated intoo ic elements of acommonly used to demonstrate document or visual presentation. In publishing and graphic design, lorem ipsum is a filler text commonly used to demonstrate the graphic elements of a document or visual presentation. Replacing meaningful content with place commonly used to view quickly-generated intoo ic elements of acommonly used to demonstrate document or visual presentation.</p>
<div class="abs q-dots"><i></i><i></i><i></i></div>
<div class="abs quote-by">- Daniel Whitfield</div>

<section class="abs newsletter">
  <svg style="position:absolute;left:72px;top:30px" width="70" height="36" viewBox="0 0 70 36"><g fill="none" stroke="#fff" stroke-width="2"><rect x="24" y="4" width="42" height="28"/><polyline points="24,4 45,20 66,4"/><line x1="2" y1="12" x2="18" y2="12"/><line x1="8" y1="20" x2="18" y2="20"/><line x1="0" y1="28" x2="18" y2="28"/></g></svg>
  <div class="nl-title">Subscribe<br>Our Newsletter</div>
  <div class="nl-input">Enter Your Email</div>
  <div class="nl-btn">SUBSCRIBE</div>
  <div class="stay">Stay<br>Connected</div>
  <div class="stay-icons"><span></span><span></span><span></span></div>
</section>

<footer class="abs footer">
  <div class="fcol" style="left:72px">
    <h4>Recent Blog</h4>
    <div class="post"><small>10 MAR 2015 | 10 Comments</small><p>Mirum est notare quam littera gothi ca, quam nunc</p></div>
    <div class="post"><small>10 MAR 2015 | 10 Comments</small><p>Mirum est notare quam littera gothi ca, quam nunc</p></div>
  </div>
  <div class="fcol" style="left:343px">
    <h4>Recent News</h4>
    <div class="post"><small>10 MAR 2015</small><p>Mirum est notare quam littera gothi ca, quam nunc</p></div>
    <div class="post"><small>10 MAR 2015</small><p>Mirum est notare quam littera gothi ca, quam nunc</p></div>
  </div>
  <div class="fcol" style="left:613px">
    <h4>Get in Touch</h4>
    <div class="touch"><span><svg width="12" height="16" viewBox="0 0 12 16"><path d="M6 15C2 9 1 7.5 1 5.5a5 5 0 0 1 10 0C11 7.5 10 9 6 15z" fill="#fff"/><circle cx="6" cy="5.5" r="1.8" fill="#555"/></svg></span><div>228, Lorem Ipsum,<br>Dolor sit, 898585-Lorem</div></div>
    <div class="touch"><span><svg width="14" height="14" viewBox="0 0 14 14"><path d="M3 1l2.5 3-1.5 1.5a8 8 0 0 0 4.5 4.5L10 8.5l3 2.5-1.5 2C6 13 1 8 1 2.5z" fill="#fff"/></svg></span><div>Phone :<br>1-800-555-0142</div></div>
    <div class="touch"><span><svg width="14" height="11" viewBox="0 0 14 11"><rect x="1" y="1" width="12" height="9" fill="none" stroke="#fff" stroke-width="1.4"/><polyline points="1,1 7,6 13,1" fill="none" stroke="#fff" stroke-width="1.4"/></svg></span><div>Email :<br>info@lumoraeyecare.com</div></div>
  </div>
  <div class="f-brand"><span class="brand-dot"></span><span class="brand-name">LUMORA EYE</span></div>
  <div class="legal">© 2015 Lumora Eye Care.<br>All Rights Reserved. Terms &amp; Conditions<br>Privacy Policy | Terms of Use</div>
</footer>

</body>
</html>
```